WTR PDAK Thank You card

We need a thank you card to give to our various stakeholders. The card design needs to be professional, corporate, and use elements of our current visual identity (colours and logo will be supplied). The inside of the card needs to have a space for a personal message to be written. Our target card size is 5 x 7.

As a bit of background, we fund local health care in Provincia. We do not directly provide front-line health care services. We do manage the funding and performance monitoring for the agencies we fund. We engage a wide range of people from CEO's, to MPP's, to the general public on a variety of health care topics. At the heart of it, we are a local organization that works to improve health care in Windsor/Essex, Chatham-Kent, and Sarnia/Lambton.

The final design should lean towards a more traditional look.

• It must incorporate our colour pallet and logo

```html
<!DOCTYPE html>
<html lang="en">
<head>
<meta charset="utf-8">
<title>WTR PDAK Thank You Card</title>
<link rel="stylesheet" href="https://fonts.googleapis.com/css2?family=Arimo:wght@400;700&family=Parisienne&display=swap">
<style>
  :root {
    --orange: #e07b22;
    --orange-deep: #d8741c;
    --grey: #818285;
    --grey-dots: #8b8b8e;
    --white: #ffffff;
    --ink: #111111;
  }
  * { margin: 0; padding: 0; box-sizing: border-box; }
  html, body { width: 857px; height: 1200px; overflow: hidden; background: var(--white); }
  .card { position: relative; width: 857px; height: 1200px; overflow: hidden; background: var(--white); font-family: "Arimo", Arial, sans-serif; }

  .pattern {
    position: absolute; left: 0; width: 857px;
    background: radial-gradient(circle at 30% 40%, var(--orange) 0%, var(--orange-deep) 55%, var(--grey-dots) 140%);
  }
  .pattern--top { top: 0; height: 310px; }
  .pattern--lower { top: 386px; height: 214px; background: linear-gradient(180deg, var(--orange) 0%, var(--orange-deep) 60%, var(--grey-dots) 100%); }

  .band { position: absolute; left: 0; top: 300px; width: 857px; height: 95px; background: var(--orange); }

  .message-area { position: absolute; left: 0; top: 600px; width: 857px; height: 340px; background: var(--grey); }

  .greeting {
    position: absolute; left: 322px; top: 345px;
    font-family: "Parisienne", cursive; font-size: 150px; line-height: 1; white-space: nowrap;
  }
  .greeting__thank { color: var(--ink); }
  .greeting__you { color: var(--white); margin-left: 18px; }

  .write-line { position: absolute; height: 3px; background: var(--white); }
  .write-line--short { left: 300px; width: 517px; top: 683px; }
  .write-line--full { left: 33px; width: 784px; }

  .signature-block { position: absolute; left: 496px; top: 960px; }
  .signature-block__mark { position: absolute; left: 0; top: 6px; width: 62px; height: 62px; background: var(--ink); }
  .signature-block__text { position: absolute; left: 84px; top: 0; width: 230px; color: var(--ink); }
  .signature-block__name { font-size: 50px; font-weight: 400; line-height: 1.1; letter-spacing: -0.5px; border-bottom: 2px solid var(--ink); padding-bottom: 4px; }
  .signature-block__en { font-size: 15px; font-weight: 700; line-height: 1.25; padding: 6px 0 5px; border-bottom: 1.5px solid var(--ink); }
  .signature-block__fr { font-size: 15px; font-weight: 700; line-height: 1.25; padding-top: 5px; }
</style>
</head>
<body>
<main class="card">
  <div class="pattern pattern--top" role="img" aria-label="Decorative pattern of overlapping orange circles on grey"></div>
  <div class="pattern pattern--lower" role="img" aria-label="Decorative pattern of overlapping orange circles fading into grey"></div>
  <div class="band"></div>
  <div class="message-area"></div>

  <h1 class="greeting"><span class="greeting__thank">thank</span><span class="greeting__you">you</span></h1>

  <div class="write-line write-line--short"></div>
  <div class="write-line write-line--full" style="top:726px"></div>
  <div class="write-line write-line--full" style="top:766px"></div>
  <div class="write-line write-line--full" style="top:807px"></div>
  <div class="write-line write-line--full" style="top:847px"></div>

  <footer class="signature-block">
    <div class="signature-block__mark"></div>
    <div class="signature-block__text">
      <p class="signature-block__name">Provincia</p>
      <p class="signature-block__en">WTR PDAK Local Health<br>Integration Network</p>
      <p class="signature-block__fr">Réseau local d’intégration<br>des services de santé<br>WTR PDAK</p>
    </div>
  </footer>
</main>
</body>
</html>
```